Book cover design for a collection of poetry - The Lanternfield

Book cover and back design need to be moody, nostalgic, reflective, ethereal. Melancholy and other worldly. Cover design should not be time specific to a period or place but if applicable should reflect British landscape. Book cover should be in tones of blue and must include the title and author (THE LANTERNFIELD BY DORIAN WELKBRIDGE). We love the idea of rain, and looking out of a window. See attached designs. A world you are observing but not in.

Industry/Entity Type

Book Publisher

Font styles to use
Serif
Script

Colors
3176b5
3377b5
85acd3
eaf1f7
0792cd
33a6d7
86cae7
ecf7fb
86cfc6

Requirements
Must have
• The colour blue in it, must be melancholy and reflective.
Nice to have
• Rain in the cover.
Should not have
• Any bright colours.

```html
<!DOCTYPE html>
<html lang="en">
<head>
<meta charset="utf-8">
<title>The Lanternfield – Book Cover</title>
<link rel="stylesheet" href="https://fonts.googleapis.com/css2?family=Great+Vibes&family=Alegreya:wght@400;700&family=Alegreya+SC&display=swap">
<style>
  :root {
    --ink: #ffffff;
    --ink-soft: #eaf1f7;
    --teal-light: #4f8a8d;
    --teal-mid: #2e5e63;
    --teal-deep: #17343a;
    --night: #0f1e24;
    --ember: #b3122a;
    --shadow: rgba(5, 20, 28, 0.75);
  }
  * { margin: 0; padding: 0; box-sizing: border-box; }
  html, body { width: 1200px; height: 900px; overflow: hidden; background: var(--night); }
  .cover {
    position: relative;
    width: 1200px;
    height: 900px;
    overflow: hidden;
    color: var(--ink);
    font-family: "Alegreya", Georgia, serif;
  }
  .cover__photo {
    position: absolute; inset: 0;
    background:
      radial-gradient(ellipse 70px 60px at 1070px 700px, rgba(179,18,42,0.75), transparent 80%),
      radial-gradient(ellipse 90px 80px at 870px 720px, rgba(179,18,42,0.8), transparent 80%),
      radial-gradient(ellipse 110px 90px at 330px 760px, rgba(179,18,42,0.55), transparent 80%),
      radial-gradient(ellipse 60px 70px at 600px 500px, rgba(179,18,42,0.35), transparent 80%),
      linear-gradient(180deg, var(--teal-light) 0%, var(--teal-mid) 35%, var(--teal-deep) 65%, var(--night) 100%);
  }

  /* Back cover */
  .back { position: absolute; left: 0; top: 0; width: 565px; height: 900px; }
  .back__title {
    position: absolute; left: 0; width: 565px; top: 28px;
    font-family: "Great Vibes", cursive; font-weight: 400;
    text-align: center; line-height: 0.8; font-size: 58px;
  }
  .back__title span { display: block; }
  .back__title .the { font-size: 46px; margin-left: -40px; }
  .back__blurb-caps {
    position: absolute; left: 20px; width: 530px;
    font-size: 14px; letter-spacing: 3.6px; line-height: 18px;
    text-align: center; text-transform: uppercase; font-weight: 700;
  }
  .back__blurb-caps--one { top: 146px; }
  .back__blurb-caps--two { top: 382px; }
  .back__blurb {
    position: absolute; left: 24px; top: 493px; width: 528px;
    font-family: "Alegreya SC", Georgia, serif;
    font-size: 14.5px; line-height: 20px; text-align: justify;
  }
  .back__blank { position: absolute; left: 352px; top: 727px; width: 199px; height: 120px; background: var(--ink); }

  /* Spine */
  .spine { position: absolute; left: 565px; top: 0; width: 75px; height: 900px; }
  .spine__title, .spine__author {
    position: absolute; left: 37px; white-space: nowrap;
    transform-origin: 0 0; transform: rotate(90deg);
  }
  .spine__title { top: 45px; font-family: "Great Vibes", cursive; font-size: 40px; margin-left: 22px; }
  .spine__author { top: 490px; font-size: 32px; font-weight: 700; margin-left: 18px; letter-spacing: 0.5px; }

  /* Front cover */
  .front { position: absolute; left: 640px; top: 0; width: 560px; height: 900px; }
  .front__title {
    position: absolute; left: 10px; top: 90px;
    font-family: "Great Vibes", cursive; font-weight: 400;
    text-shadow: 3px 5px 8px var(--shadow); line-height: 1;
  }
  .front__title .the { display: block; font-size: 56px; margin-left: 14px; }
  .front__title .main { display: block; font-size: 96px; margin-top: -14px; white-space: nowrap; }
  .front__tagline {
    position: absolute; right: 42px; top: 232px;
    font-size: 30px; text-shadow: 2px 3px 5px var(--shadow);
  }
  .front__rule { position: absolute; left: 12px; width: 461px; height: 2px; background: var(--ink-soft); }
  .front__rule--top { top: 299px; }
  .front__rule--bottom { top: 382px; }
  .front__author {
    position: absolute; left: 12px; width: 461px; top: 314px;
    font-size: 40px; font-weight: 700; text-align: center; white-space: nowrap;
    text-shadow: 2px 3px 5px var(--shadow);
  }
</style>
</head>
<body>
<main class="cover">
  <div class="cover__photo" role="img" aria-label="Photograph of rain running down a window at dusk, blue-green glass with blurred red lights behind"></div>

  <section class="back">
    <h2 class="back__title"><span class="the">The</span><span>Lanternfield</span></h2>
    <p class="back__blurb-caps back__blurb-caps--one">The Lanternfield is a collection of poetry.<br><br>Told in two parts we first meet Charles – aged, crippled and left alone in his inherited marsh house – reflecting on his life and his marriage to beautiful Alice who we meet in part two. Alice is suicidal, manically depressed and struggling with life as a wife and mother. She meets, harbors and falls in love with a soldier during WWII and her world is changed forever.</p>
    <p class="back__blurb-caps back__blurb-caps--two">Moving through the 20th century, this life and the next, The Lanternfield interweaves grief, loss, the after-life, mental illness, and ultimately the true nature of love.</p>
    <p class="back__blurb">The Lanternfield is a collection of poetry documenting the lives of an aristocratic couple throughout the 20th Century. Told in two parts we first meet Charles – aged, crippled and left alone in his inherited Marsh House – reflecting on his life and his marriage to beautiful Alice who we meet in part two. Alice is suicidal, manically depressed and struggling with societal conventions and life as a wife and mother. She meets, harbors and falls in love with a soldier during WWII and her world is changed forever. Moving through decades, through this life and the next – The Lanternfield interweaves themes of grief, loss, the after-life, mental illness, and ultimately the true nature of love.</p>
    <div class="back__blank"></div>
  </section>

  <section class="spine">
    <div class="spine__title">The Lanternfield</div>
    <div class="spine__author">DORIAN WELKBRIDGE</div>
  </section>

  <section class="front">
    <h1 class="front__title"><span class="the">The</span><span class="main">Lanternfield</span></h1>
    <p class="front__tagline">A collection of poetry.</p>
    <div class="front__rule front__rule--top"></div>
    <p class="front__author">DORIAN WELKBRIDGE</p>
    <div class="front__rule front__rule--bottom"></div>
  </section>
</main>
</body>
</html>
```